We are needing a bookcover for a reprint of our book "Whispers Beneath the Cobalt Ridgelands". It takes a look at the geologic formation found in the great plains. Our original cover was colorful and showed rock layers. Something similar but different and eye catching would be great. a geologic cross section showing various layers or possibly some different rocks/soils. We are really open to suggestions attached is the current book cover with the colored layers and the cover from the 80s.

Target Market(s)

Adult Readers

Industry/Entity Type

Nonprofit retail - science - nature

Requirements
Must have
• Geology or rock layers
Nice to have
• Books title, Geologic cross section
Should not have
• People or animals, no photos prefer sketch

```html
<!DOCTYPE html>
<html lang="en">
<head>
<meta charset="utf-8">
<title>Whispers Beneath the Cobalt Ridgelands – Cover Options</title>
<link href="https://fonts.googleapis.com/css2?family=Open+Sans:wght@600;700;800&display=swap" rel="stylesheet">
<style>
  :root {
    --page-bg: #ffffff;

    --color-bg: #bfcb76;
    --color-title-accent: #6b2008;
    --color-title-main: #2d4a43;
    --color-title-light: #ffffff;

    --mono-bg: #cbcbcb;
    --mono-title-dark: #4a4a4a;
    --mono-title-light: #efefef;

    --author-text: #ffffff;
  }

  * { margin: 0; padding: 0; box-sizing: border-box; }

  html, body {
    width: 1200px;
    height: 950px;
    overflow: hidden;
    background: var(--page-bg);
    font-family: "Open Sans", Arial, sans-serif;
  }

  .cover-sheet {
    position: relative;
    width: 1200px;
    height: 950px;
  }

  .cover {
    position: absolute;
    top: 132px;
    width: 458px;
    height: 681px;
    overflow: hidden;
  }
  .cover--color { left: 134px; background: var(--color-bg); }
  .cover--mono  { left: 651px; background: var(--mono-bg); }

  .cover__artwork {
    position: absolute;
    left: 0;
    right: 0;
    top: 236px;
    bottom: 0;
  }
  .cover--color .cover__artwork {
    background: linear-gradient(180deg,
      #bfcb76 0%,
      #7f9d5e 6%,
      #ddd3b4 12%,
      #e8973f 22%,
      #d9622a 34%,
      #a89560 44%,
      #5d6768 58%,
      #3f5460 70%,
      #c1503a 84%,
      #a94436 100%);
  }
  .cover--mono .cover__artwork {
    background: linear-gradient(180deg,
      #cbcbcb 0%,
      #6e6e6e 6%,
      #dedede 12%,
      #a8a8a8 24%,
      #7a7a7a 40%,
      #4f4f4f 58%,
      #333333 76%,
      #1e1e1e 100%);
  }

  .cover__title {
    position: absolute;
    top: 30px;
    left: 0;
    right: 0;
    text-align: center;
    font-weight: 800;
    text-transform: uppercase;
    line-height: 1;
    letter-spacing: -0.5px;
  }
  .cover__title span { display: block; }

  .title-line--small { font-size: 32px; margin-bottom: 6px; }
  .title-line--accent { font-size: 44px; margin-bottom: 6px; }
  .title-line--main { font-size: 52px; }

  .cover--color .title-line--small  { color: var(--color-title-light); }
  .cover--color .title-line--accent { color: var(--color-title-accent); }
  .cover--color .title-line--main   { color: var(--color-title-main); }

  .cover--mono .title-line--small  { color: var(--mono-title-light); }
  .cover--mono .title-line--accent { color: var(--mono-title-dark); }
  .cover--mono .title-line--main   { color: var(--mono-title-dark); }

  .cover__author {
    position: absolute;
    top: 589px;
    left: 0;
    width: 460px;
    text-align: center;
    color: var(--author-text);
  }
  .author__label {
    display: block;
    font-size: 15px;
    font-weight: 600;
    letter-spacing: 0.5px;
  }
  .author__name {
    display: block;
    margin-top: 4px;
    font-size: 12px;
    font-weight: 600;
    letter-spacing: 0.55em;
  }
</style>
</head>
<body>
  <main class="cover-sheet">

    <section class="cover cover--color">
      <div class="cover__artwork" role="img" aria-label="Illustration of a cut-away block of land with small evergreen trees on a grassy top and stacked rock strata in orange, ochre, slate blue and red, split by fissures"></div>
      <h1 class="cover__title">
        <span class="title-line--small">Whispers</span>
        <span class="title-line--accent">Beneath the</span>
        <span class="title-line--small">Cobalt</span>
        <span class="title-line--main">Ridgelands</span>
      </h1>
      <p class="cover__author">
        <span class="author__label">written by</span>
        <span class="author__name">Mara Ellison</span>
      </p>
    </section>

    <section class="cover cover--mono">
      <div class="cover__artwork" role="img" aria-label="Greyscale halftone illustration of a cut-away block of land with evergreen trees on top and stacked rock strata split by fissures"></div>
      <h2 class="cover__title">
        <span class="title-line--small">Whispers</span>
        <span class="title-line--accent">Beneath the</span>
        <span class="title-line--small">Cobalt</span>
        <span class="title-line--main">Ridgelands</span>
      </h2>
      <p class="cover__author">
        <span class="author__label">written by</span>
        <span class="author__name">Mara Ellison</span>
      </p>
    </section>

  </main>
</body>
</html>
```